Buchcover-Design für Coaching-Buch
Zielgruppe
22 Coaches (m/w/d) haben zusammen ein Buch geschrieben - mit ihren besten Tipps, Mut machenden Geschichten und Inspirationen. Herausgekommen ist 'Die stille Mentorin am Fensterbrett - 22 Schatzkisten lüften ihre Rätsel'. Zielgruppe sind vorwiegend Frauen, häufig mit spirituellem Hintergrund oder an Selbstentwicklung interessiert, sowie Menschen, die sich ermutigen lassen möchten und Menschen, die inspirierende Texte und Geschichten mögen. Die Themen sind ganz unterschiedlich, von Selbstliebe über die Wirkung von Farben, vom Überwinden von Krisen und Angst, Umgang mit Emotionen etc. pp. - ein ganzer Blumenstrauß an Themen.
Aufgabenstellung
Der Titel 'Die stille Mentorin am Fensterbrett' kam auf, weil wir die Vorstellung hatten, dass in dem Buch vielleicht abends im Bett gelesen wird und man dann ruhig schlafen kann.
Warum Füllhörner? Nun, jeder Coach hat viel zu geben. Zu jedem Text wird es ein Geschenk geben, das die Autor*innen online zur Verfügung stellen. Dies sind PDFs mit Tipps, Meditationen oder sogar eine kurze Gratis-Session. Es braucht also etwas auf dem Cover, das darauf hindeutet, vielleicht eine Plakette oder etwas Ähnliches, das 'Mit 22 Geschenken' besagt. Im Buchsatz wird dies durch einen Link (E-Book) und durch einen QR-Code (Print) umgesetzt.

```html
<!DOCTYPE html>
<html lang="de">
<head>
<meta charset="utf-8">
<title>Die stille Mentorin am Fensterbrett – Buchcover</title>
<link href="https://fonts.googleapis.com/css2?family=Amatic+SC:wght@700&family=Jost:wght@400&display=swap" rel="stylesheet">
<style>
  :root {
    --stage: #efe6e1;
    --coral: #e8825f;
    --coral-soft: #e99780;
    --coral-pale: #eaa895;
    --taupe: #615950;
    --ink-light: #f3efec;
  }
  html, body {
    margin: 0;
    padding: 0;
    width: 1200px;
    height: 675px;
    overflow: hidden;
    background: var(--stage);
  }
  .canvas {
    position: relative;
    width: 1200px;
    height: 675px;
  }
  .book-cover {
    position: absolute;
    left: 406px;
    top: 136px;
    width: 415px;
    height: 384px;
  }
  .cover-pattern {
    position: absolute;
    inset: 0;
    background: linear-gradient(135deg, var(--coral) 0%, var(--coral-soft) 50%, var(--coral-pale) 100%);
  }
  .cover-type {
    position: absolute;
    inset: 0;
    width: 100%;
    height: 100%;
    display: block;
  }
  .cover-title {
    font-family: "Amatic SC", cursive;
    font-weight: 700;
    fill: var(--ink-light);
  }
  .cover-subtitle {
    font-family: "Jost", sans-serif;
    font-weight: 400;
    fill: var(--ink-light);
  }
  .badge-number {
    font-family: "Amatic SC", cursive;
    font-weight: 700;
    fill: var(--ink-light);
  }
  .badge-label {
    font-family: "Jost", sans-serif;
    fill: var(--ink-light);
  }
</style>
</head>
<body>
<main class="canvas">
  <section class="book-cover">
    <div class="cover-pattern" role="img" aria-label="Organisches Wellenmuster in Koralle, Lachsrosa und Taupe"></div>
    <svg class="cover-type" viewBox="0 0 665 615" xmlns="http://www.w3.org/2000/svg" role="img" aria-label="Die stille Mentorin am Fensterbrett – 22 Schatzkisten lüften ihre Rätsel, 22 Geschenke im Buch">
      <defs>
        <path id="title-arc" d="M150 250 Q340 95 532 250"/>
      </defs>

      <g class="gift-badge">
        <circle cx="566" cy="88" r="63" fill="var(--taupe)"/>
        <text class="badge-number" x="566" y="86" text-anchor="middle" font-size="50">22</text>
        <text class="badge-label" x="566" y="108" text-anchor="middle" font-size="14">Geschenke</text>
        <text class="badge-label" x="566" y="125" text-anchor="middle" font-size="14">im Buch</text>
      </g>

      <text class="cover-title" font-size="48" letter-spacing="2">
        <textPath href="#title-arc" startOffset="50%" text-anchor="middle">DIE STILLE MENTORIN</textPath>
      </text>
      <text class="cover-title" x="343" y="270" text-anchor="middle" font-size="50" letter-spacing="2">AM</text>
      <text class="cover-title" x="343" y="378" text-anchor="middle" font-size="104" textLength="428" lengthAdjust="spacingAndGlyphs">FENSTERBRETT</text>
      <text class="cover-subtitle" x="347" y="438" text-anchor="middle" font-size="19">22 Schatzkisten lüften ihre Rätsel</text>
    </svg>
  </section>
</main>
</body>
</html>
```